Redesign our iOS App Design mockups

- Redesign our current Veltro App Mockup
- Keep the design simple so that programmers do not have to do too much extra work to make your design work.
- Look at the attached website screenshot for the overall look and feel, and color scheme
- Convert the attached vector logo to iOS Icon format.
- Deliver all graphics in the density required for Veltro QL Prime.
- I have attached the current iOS mockup in a .ZIP file but you can view it here as well: https://boards.mockvault.net/share/QWTRPL8HNB2

Target Market(s)

Mostly Male Internet Consumers between the ages of 20 and 35

Industry/Entity Type

Internet

Colors

Designer to choose colors to be used in the design.

Requirements
Must have
• - Deliver all graphics in the density required for Veltro QL Prime
• - Should also look good on Tabrix and Tabrix pro
• - Design type should be “FLAT.”
• - Spell out fonts used in the design and where they are used. Also, include font sizes.
• - Please use ALL the elements in each page and use all placements and text EXACTLY. Please do not improvise with text or components.
• I have designed the mockup exactly the way I like it. I just want it to made to look better.
Should not have

```html
<!DOCTYPE html>
<html lang="en">
<head>
<meta charset="utf-8">
<title>Hushnet iOS App Screens</title>
<link href="https://fonts.googleapis.com/css2?family=Lato:wght@300;400;700&display=swap" rel="stylesheet">
<style>
  :root{
    --coral:#f45d4c;
    --navy:#17377b;
    --ink:#2f2f2f;
    --muted:#9a9a9a;
    --faint:#c4c4c4;
    --rule:#d9d9d9;
    --dim:#9c9c9c;
    --star:#b8b8b8;
    --gold:#f5a623;
    --paper:#ffffff;
  }
  *{box-sizing:border-box;margin:0;padding:0}
  html,body{width:1200px;height:720px;overflow:hidden;background:var(--paper)}
  body{position:relative;font-family:'Lato',sans-serif;color:var(--ink)}
  .screen{position:absolute;background:var(--paper);overflow:hidden;box-shadow:0 6px 28px rgba(0,0,0,.09)}
  .screen *{position:absolute;line-height:1;white-space:nowrap}
  .coral{background:var(--coral)}
  .header{left:0;top:0;width:100%;height:48px;background:var(--coral)}
  .time{left:21px;top:11px;font-size:7px;font-weight:700;color:#fff}
  .status{right:10px;top:11px}
  .back{left:20px;top:29px}
  .title{left:0;width:100%;top:30px;text-align:center;font-size:7.5px;font-weight:700;color:#fff}
  .label{font-size:5.5px;letter-spacing:.2px;color:var(--muted);text-transform:uppercase}
  .rule{height:1px;background:var(--rule)}
  .row{font-size:8.5px;color:var(--ink)}
  .chev{width:6px;height:8px}
  .star{width:7px;height:7px}
  .flag{width:21px;height:21px;border-radius:50%;overflow:hidden;box-shadow:inset 0 0 0 .5px rgba(0,0,0,.1)}
  .brand{font-weight:700;letter-spacing:-.2px}
  .brand-dot{border-radius:50%}

  /* splash */
  .splash{left:34px;top:119px;width:206px;height:447px;background:var(--coral)}
  .splash .brand-dot{left:85px;top:176px;width:36px;height:36px;background:#fff}
  .splash .brand{left:0;width:100%;top:226px;text-align:center;font-size:13px;color:#fff}

  /* login */
  .login{left:266px;top:7px;width:206px;height:447px}
  .login .brand-dot{left:90px;top:78px;width:24px;height:24px;background:var(--coral)}
  .login .brand{left:0;width:100%;top:118px;text-align:center;font-size:9px;color:var(--ink)}
  .field-line{height:1px}
  .login .email-line{left:39px;top:196px;width:125px;background:var(--coral)}
  .login .pass-line{left:39px;top:229px;width:125px;background:var(--rule)}
  .placeholder{font-size:7.5px;color:var(--faint);font-weight:300}
  .caret{width:1px;height:10px;background:var(--ink)}
  .forgot-link{right:42px;top:237px;font-size:8px;color:var(--coral)}
  .btn-login{left:38px;top:287px;width:128px;height:36px;background:var(--coral);color:#fff;font-size:9.5px;font-weight:300;display:flex;align-items:center;justify-content:center}
  .create{left:0;width:100%;top:335px;text-align:center;font-size:8.5px;color:var(--coral);font-weight:300}

  /* forgot */
  .forgot{left:266px;top:478px;width:204px;height:242px}
  .forgot .headline{left:25px;top:114px;font-size:13.5px;font-weight:400;line-height:1.25;white-space:normal;width:160px}
  .forgot .copy{left:25px;top:155px;width:140px;font-size:6px;line-height:9px;color:var(--dim);white-space:normal;font-weight:300}
  .forgot .email-line{left:26px;top:237px;width:152px;background:var(--coral)}

  /* home */
  .home{left:493px;top:127px;width:206px;height:499px}
  .navbar{left:0;top:48px;width:100%;height:31px;background:var(--navy)}
  .status-text{left:20px;top:59px;font-size:8.5px;color:#fff}
  .quick{left:122px;top:56px;width:62px;height:14px;border-radius:7px;background:#fff;color:var(--navy);font-size:5px;font-weight:700;display:flex;align-items:center;justify-content:center}
  .home .head-brand{left:86px;top:29px;font-size:7px;color:#fff}
  .ping{left:141px;top:31px;font-size:5px;font-weight:700;color:#fff}
  .info{left:172px;top:28px;width:10px;height:10px;border-radius:50%;background:#fff;color:var(--coral);font-size:7px;font-weight:700;display:flex;align-items:center;justify-content:center}

  /* drawer */
  .drawer{left:719px;top:32px;width:206px;height:448px;background:#9d9d9d}
  .drawer .under-head{left:0;top:0;width:100%;height:48px;background:#b24a3e}
  .drawer .under-nav{left:0;top:48px;width:100%;height:30px;background:#142a5c}
  .drawer .panel{left:0;top:0;width:153px;height:448px;background:var(--paper)}
  .drawer .brand-dot{left:23px;top:38px;width:15px;height:15px;background:var(--coral)}
  .drawer .brand{left:44px;top:42px;font-size:7.5px;color:var(--ink)}
  .menu{left:47px;font-size:8px;color:var(--muted)}
  .menu.active{color:var(--coral)}
  .icon{left:21px}
  .under-rule{height:1px;left:153px;width:30px;background:#8a8a8a}

  /* settings */
  .settings{left:721px;top:501px;width:206px;height:219px}
  .toggle{left:166px;top:102px;width:16px;height:8px;border-radius:4px;background:#f8c5bf}
  .toggle i{position:absolute;right:-1px;top:-1px;width:10px;height:10px;border-radius:50%;background:var(--coral)}
  .desc{font-size:6.2px;color:var(--faint);line-height:9px;white-space:normal}

  /* protocols */
  .protocols{left:948px;top:222px;width:209px;height:453px}
</style>
</head>
<body>

<!-- Splash -->
<section class="screen splash" aria-label="Splash screen">
  <span class="brand-dot"></span>
  <span class="brand">HUSHNET</span>
</section>

<!-- Login -->
<section class="screen login" aria-label="Login screen">
  <span class="brand-dot"></span>
  <span class="brand">HUSHNET</span>
  <svg style="left:43px;top:183px" width="8" height="6" viewBox="0 0 8 6"><rect x=".5" y=".5" width="7" height="5" fill="none" stroke="#f45d4c" stroke-width=".8"/><path d="M.5 .5L4 3.3 7.5 .5" fill="none" stroke="#f45d4c" stroke-width=".8"/></svg>
  <span class="caret" style="left:56px;top:182px"></span>
  <span class="placeholder" style="left:60px;top:184px;color:#eee">Email</span>
  <span class="field-line email-line"></span>
  <svg style="left:43px;top:214px" width="7" height="9" viewBox="0 0 7 9"><rect x=".5" y="3.8" width="6" height="4.7" fill="none" stroke="#c4c4c4" stroke-width=".8"/><path d="M1.8 3.8V2.4a1.7 1.7 0 0 1 3.4 0v1.4" fill="none" stroke="#c4c4c4" stroke-width=".8"/></svg>
  <span class="placeholder" style="left:56px;top:217px">Password</span>
  <span class="field-line pass-line"></span>
  <span class="forgot-link">Forgot Password</span>
  <div class="btn-login">Log In</div>
  <span class="create">Create an account</span>
</section>

<!-- Forgot password -->
<section class="screen forgot" aria-label="Forgot password screen">
  <div class="header"></div>
  <span class="time">9:41</span>
  <svg class="status" width="32" height="7" viewBox="0 0 32 7"><rect x="0" y="5" width="1.5" height="2" fill="#fff"/><rect x="2.3" y="3.5" width="1.5" height="3.5" fill="#fff"/><rect x="4.6" y="2" width="1.5" height="5" fill="#fff"/><rect x="6.9" y=".5" width="1.5" height="6.5" fill="#fff"/><path d="M11 3a5 5 0 0 1 7 0M12.3 4.4a3 3 0 0 1 4.4 0" stroke="#fff" stroke-width="1" fill="none"/><circle cx="14.5" cy="6" r=".9" fill="#fff"/><rect x="21" y="1" width="9.5" height="5" rx="1" fill="#fff"/><rect x="30.8" y="2.6" width="1" height="1.8" fill="#fff"/></svg>
  <svg class="back" width="6" height="9" viewBox="0 0 6 9"><polyline points="5,1 1.5,4.5 5,8" fill="none" stroke="#fff" stroke-width="1.2"/></svg>
  <span class="title">Forgot Password</span>
  <h1 class="headline">Did you forget your Password?</h1>
  <p class="copy">If you have forgotten your password, enter the email address associated with your account into the box below and we will send you instructions on how to reset your password to your email account</p>
  <svg style="left:30px;top:226px" width="8" height="6" viewBox="0 0 8 6"><rect x=".5" y=".5" width="7" height="5" fill="none" stroke="#f45d4c" stroke-width=".8"/><path d="M.5 .5L4 3.3 7.5 .5" fill="none" stroke="#f45d4c" stroke-width=".8"/></svg>
  <span class="caret" style="left:46px;top:224px;height:9px"></span>
  <span class="placeholder" style="left:50px;top:226px;color:#eee">Email</span>
  <span class="field-line email-line"></span>
</section>

<!-- Home -->
<section class="screen home" aria-label="Home screen">
  <div class="header"></div>
  <span class="time">9:41</span>
  <svg class="status" width="32" height="7" viewBox="0 0 32 7"><rect x="0" y="5" width="1.5" height="2" fill="#fff"/><rect x="2.3" y="3.5" width="1.5" height="3.5" fill="#fff"/><rect x="4.6" y="2" width="1.5" height="5" fill="#fff"/><rect x="6.9" y=".5" width="1.5" height="6.5" fill="#fff"/><path d="M11 3a5 5 0 0 1 7 0M12.3 4.4a3 3 0 0 1 4.4 0" stroke="#fff" stroke-width="1" fill="none"/><circle cx="14.5" cy="6" r=".9" fill="#fff"/><rect x="21" y="1" width="9.5" height="5" rx="1" fill="#fff"/><rect x="30.8" y="2.6" width="1" height="1.8" fill="#fff"/></svg>
  <svg style="left:21px;top:29px" width="11" height="8" viewBox="0 0 11 8"><path d="M0 .5h11M0 4h9M0 7.5h6" stroke="#fff" stroke-width="1"/></svg>
  <span class="brand head-brand">HUSHNET</span>
  <span class="ping">PING TEST</span>
  <span class="info">i</span>
  <div class="navbar"></div>
  <span class="status-text">Not Connected</span>
  <div class="quick">QUICK CONNECT</div>

  <span class="label" style="left:21px;top:103px">Favorites</span>
  <span class="rule" style="left:21px;top:115px;width:182px"></span>
  <span class="flag" style="left:21px;top:126px;background:linear-gradient(#111 33%,#dd0000 33% 66%,#ffce00 66%)"></span>
  <span class="row" style="left:50px;top:132px">Germany</span>
  <svg class="chev" style="left:174px;top:132px" viewBox="0 0 6 8"><polyline points="1,.8 4.5,4 1,7.2" fill="none" stroke="#555" stroke-width="1"/></svg>

  <span class="label" style="left:21px;top:175px">Specialty Servers</span>
  <span class="rule" style="left:21px;top:187px;width:182px"></span>
  <span class="row" style="left:21px;top:199px">Streaming Servers</span>
  <svg class="chev" style="left:174px;top:199px" viewBox="0 0 6 8"><polyline points="1,.8 4.5,4 1,7.2" fill="none" stroke="#555" stroke-width="1"/></svg>
  <span class="row" style="left:21px;top:221px">P2P Servers</span>
  <svg class="chev" style="left:174px;top:221px" viewBox="0 0 6 8"><polyline points="1,.8 4.5,4 1,7.2" fill="none" stroke="#555" stroke-width="1"/></svg>
  <span class="row" style="left:21px;top:243px">Onion Over VPN</span>
  <svg class="chev" style="left:174px;top:243px" viewBox="0 0 6 8"><polyline points="1,.8 4.5,4 1,7.2" fill="none" stroke="#555" stroke-width="1"/></svg>

  <span class="label" style="left:21px;top:280px">Favorites</span>
  <span class="rule" style="left:21px;top:292px;width:182px"></span>

  <span class="flag" style="left:21px;top:303px;background:linear-gradient(90deg,#2a3f8f 45%,transparent 45%) top left/100% 50% no-repeat,repeating-linear-gradient(#d9262f 0 3px,#fff 3px 6px)"></span>
  <span class="row" style="left:50px;top:309px">USA</span>
  <svg class="star" style="left:158px;top:309px" viewBox="0 0 10 10"><polygon points="5,0 6.2,3.6 10,3.6 6.9,5.8 8.1,9.5 5,7.2 1.9,9.5 3.1,5.8 0,3.6 3.8,3.6" fill="#b8b8b8"/></svg>
  <svg class="chev" style="left:174px;top:309px" viewBox="0 0 6 8"><polyline points="1,.8 4.5,4 1,7.2" fill="none" stroke="#555" stroke-width="1"/></svg>

  <span class="flag" style="left:21px;top:329px;background:linear-gradient(#c8102e,#c8102e) center/3px 100% no-repeat,linear-gradient(#c8102e,#c8102e) center/100% 3px no-repeat,linear-gradient(#fff,#fff) center/7px 100% no-repeat,linear-gradient(#fff,#fff) center/100% 7px no-repeat,#1f3a93"></span>
  <span class="row" style="left:50px;top:335px">UK</span>
  <svg class="star" style="left:158px;top:335px" viewBox="0 0 10 10"><polygon points="5,0 6.2,3.6 10,3.6 6.9,5.8 8.1,9.5 5,7.2 1.9,9.5 3.1,5.8 0,3.6 3.8,3.6" fill="#b8b8b8"/></svg>
  <svg class="chev" style="left:174px;top:335px" viewBox="0 0 6 8"><polyline points="1,.8 4.5,4 1,7.2" fill="none" stroke="#555" stroke-width="1"/></svg>

  <span class="flag" style="left:21px;top:354px;background:radial-gradient(circle,#d52b1e 0 2.5px,transparent 3px),linear-gradient(90deg,#d52b1e 27%,#fff 27% 73%,#d52b1e 73%)"></span>
  <span class="row" style="left:50px;top:360px">Canada</span>
  <svg class="star" style="left:158px;top:360px" viewBox="0 0 10 10"><polygon points="5,0 6.2,3.6 10,3.6 6.9,5.8 8.1,9.5 5,7.2 1.9,9.5 3.1,5.8 0,3.6 3.8,3.6" fill="#b8b8b8"/></svg>
  <svg class="chev" style="left:174px;top:360px" viewBox="0 0 6 8"><polyline points="1,.8 4.5,4 1,7.2" fill="none" stroke="#555" stroke-width="1"/></svg>

  <span class="flag" style="left:21px;top:380px;background:radial-gradient(circle,#06038d 0 2px,transparent 2.5px),linear-gradient(#ff9933 33%,#fff 33% 66%,#138808 66%)"></span>
  <span class="row" style="left:50px;top:386px">India</span>
  <svg class="star" style="left:158px;top:386px" viewBox="0 0 10 10"><polygon points="5,0 6.2,3.6 10,3.6 6.9,5.8 8.1,9.5 5,7.2 1.9,9.5 3.1,5.8 0,3.6 3.8,3.6" fill="#b8b8b8"/></svg>
  <svg class="chev" style="left:174px;top:386px" viewBox="0 0 6 8"><polyline points="1,.8 4.5,4 1,7.2" fill="none" stroke="#555" stroke-width="1"/></svg>

  <span class="flag" style="left:21px;top:406px;background:linear-gradient(#ef3340 50%,#fff 50%)"></span>
  <span class="row" style="left:50px;top:412px">Singapore</span>
  <svg class="star" style="left:158px;top:412px" viewBox="0 0 10 10"><polygon points="5,0 6.2,3.6 10,3.6 6.9,5.8 8.1,9.5 5,7.2 1.9,9.5 3.1,5.8 0,3.6 3.8,3.6" fill="#b8b8b8"/></svg>
  <svg class="chev" style="left:174px;top:412px" viewBox="0 0 6 8"><polyline points="1,.8 4.5,4 1,7.2" fill="none" stroke="#555" stroke-width="1"/></svg>

  <span class="flag" style="left:21px;top:432px;background:linear-gradient(#111 33%,#dd0000 33% 66%,#ffce00 66%)"></span>
  <span class="row" style="left:50px;top:438px">Germany</span>
  <svg class="star" style="left:158px;top:438px" viewBox="0 0 10 10"><polygon points="5,0 6.2,3.6 10,3.6 6.9,5.8 8.1,9.5 5,7.2 1.9,9.5 3.1,5.8 0,3.6 3.8,3.6" fill="#f5a623"/></svg>
  <svg class="chev" style="left:174px;top:438px" viewBox="0 0 6 8"><polyline points="1,.8 4.5,4 1,7.2" fill="none" stroke="#555" stroke-width="1"/></svg>
</section>

<!-- Side menu -->
<section class="screen drawer" aria-label="Side menu">
  <div class="under-head"></div>
  <div class="under-nav"></div>
  <span style="left:156px;top:31px;font-size:5px;font-weight:700;color:#e9c8c3">TEST</span>
  <span style="left:172px;top:28px;width:10px;height:10px;border-radius:50%;background:#ddd"></span>
  <span style="left:150px;top:56px;width:30px;height:14px;border-radius:7px;background:#cfcfcf;font-size:5px;font-weight:700;color:#142a5c;display:flex;align-items:center;justify-content:center">ONNECT</span>
  <span class="under-rule" style="top:116px"></span>
  <span class="under-rule" style="top:188px"></span>
  <span class="under-rule" style="top:293px"></span>
  <svg class="chev" style="left:174px;top:133px" viewBox="0 0 6 8"><polyline points="1,.8 4.5,4 1,7.2" fill="none" stroke="#555" stroke-width="1"/></svg>
  <svg class="chev" style="left:174px;top:199px" viewBox="0 0 6 8"><polyline points="1,.8 4.5,4 1,7.2" fill="none" stroke="#555" stroke-width="1"/></svg>
  <svg class="chev" style="left:174px;top:222px" viewBox="0 0 6 8"><polyline points="1,.8 4.5,4 1,7.2" fill="none" stroke="#555" stroke-width="1"/></svg>
  <svg class="chev" style="left:174px;top:244px" viewBox="0 0 6 8"><polyline points="1,.8 4.5,4 1,7.2" fill="none" stroke="#555" stroke-width="1"/></svg>
  <svg class="star" style="left:158px;top:310px" viewBox="0 0 10 10"><polygon points="5,0 6.2,3.6 10,3.6 6.9,5.8 8.1,9.5 5,7.2 1.9,9.5 3.1,5.8 0,3.6 3.8,3.6" fill="#7e7e7e"/></svg>
  <svg class="chev" style="left:174px;top:310px" viewBox="0 0 6 8"><polyline points="1,.8 4.5,4 1,7.2" fill="none" stroke="#555" stroke-width="1"/></svg>
  <svg class="star" style="left:158px;top:336px" viewBox="0 0 10 10"><polygon points="5,0 6.2,3.6 10,3.6 6.9,5.8 8.1,9.5 5,7.2 1.9,9.5 3.1,5.8 0,3.6 3.8,3.6" fill="#7e7e7e"/></svg>
  <svg class="chev" style="left:174px;top:336px" viewBox="0 0 6 8"><polyline points="1,.8 4.5,4 1,7.2" fill="none" stroke="#555" stroke-width="1"/></svg>
  <svg class="star" style="left:158px;top:362px" viewBox="0 0 10 10"><polygon points="5,0 6.2,3.6 10,3.6 6.9,5.8 8.1,9.5 5,7.2 1.9,9.5 3.1,5.8 0,3.6 3.8,3.6" fill="#7e7e7e"/></svg>
  <svg class="chev" style="left:174px;top:362px" viewBox="0 0 6 8"><polyline points="1,.8 4.5,4 1,7.2" fill="none" stroke="#555" stroke-width="1"/></svg>
  <svg class="star" style="left:158px;top:387px" viewBox="0 0 10 10"><polygon points="5,0 6.2,3.6 10,3.6 6.9,5.8 8.1,9.5 5,7.2 1.9,9.5 3.1,5.8 0,3.6 3.8,3.6" fill="#7e7e7e"/></svg>
  <svg class="chev" style="left:174px;top:387px" viewBox="0 0 6 8"><polyline points="1,.8 4.5,4 1,7.2" fill="none" stroke="#555" stroke-width="1"/></svg>
  <svg class="star" style="left:158px;top:414px" viewBox="0 0 10 10"><polygon points="5,0 6.2,3.6 10,3.6 6.9,5.8 8.1,9.5 5,7.2 1.9,9.5 3.1,5.8 0,3.6 3.8,3.6" fill="#7e7e7e"/></svg>
  <svg class="chev" style="left:174px;top:414px" viewBox="0 0 6 8"><polyline points="1,.8 4.5,4 1,7.2" fill="none" stroke="#555" stroke-width="1"/></svg>
  <svg class="star" style="left:158px;top:439px" viewBox="0 0 10 10"><polygon points="5,0 6.2,3.6 10,3.6 6.9,5.8 8.1,9.5 5,7.2 1.9,9.5 3.1,5.8 0,3.6 3.8,3.6" fill="#9b6a1a"/></svg>
  <svg class="chev" style="left:174px;top:439px" viewBox="0 0 6 8"><polyline points="1,.8 4.5,4 1,7.2" fill="none" stroke="#555" stroke-width="1"/></svg>

  <div class="panel"></div>
  <span class="brand-dot"></span>
  <span class="brand">HUSHNET</span>
  <svg class="icon" style="top:86px" width="11" height="11" viewBox="0 0 11 11"><path d="M1 5L5.5 1 10 5v5.5H1z" fill="none" stroke="#f45d4c" stroke-width=".9"/><rect x="4" y="7" width="3" height="3.5" fill="none" stroke="#f45d4c" stroke-width=".8"/></svg>
  <span class="menu active" style="top:88px">Home</span>
  <svg class="icon" style="top:114px" width="11" height="11" viewBox="0 0 11 11"><circle cx="5.5" cy="5.5" r="3.6" fill="none" stroke="#b5b5b5" stroke-width="1.8" stroke-dasharray="1.6 1.2"/><circle cx="5.5" cy="5.5" r="1.6" fill="none" stroke="#b5b5b5" stroke-width=".8"/></svg>
  <span class="menu" style="top:116px">Settings</span>
  <svg class="icon" style="top:141px" width="13" height="12" viewBox="0 0 13 12"><rect x="4.5" y=".5" width="8" height="6" fill="none" stroke="#b5b5b5" stroke-width=".8"/><path d="M.5 4.5h3v1M.5 4.5v6h8V7.5" fill="none" stroke="#b5b5b5" stroke-width=".8"/></svg>
  <span class="menu" style="top:144px">Support Center</span>
  <svg class="icon" style="top:214px" width="12" height="12" viewBox="0 0 12 12"><path d="M7 1H1v10h6M1 1l4 1.5v9L1 11" fill="none" stroke="#b5b5b5" stroke-width=".8"/><path d="M8 6h4M10 4l2 2-2 2" fill="none" stroke="#b5b5b5" stroke-width=".8"/></svg>
  <span class="menu" style="top:217px">Log Out</span>
</section>

<!-- Settings -->
<section class="screen settings" aria-label="Settings screen">
  <div class="header"></div>
  <span class="time">9:41</span>
  <svg class="status" width="32" height="7" viewBox="0 0 32 7"><rect x="0" y="5" width="1.5" height="2" fill="#fff"/><rect x="2.3" y="3.5" width="1.5" height="3.5" fill="#fff"/><rect x="4.6" y="2" width="1.5" height="5" fill="#fff"/><rect x="6.9" y=".5" width="1.5" height="6.5" fill="#fff"/><path d="M11 3a5 5 0 0 1 7 0M12.3 4.4a3 3 0 0 1 4.4 0" stroke="#fff" stroke-width="1" fill="none"/><circle cx="14.5" cy="6" r=".9" fill="#fff"/><rect x="21" y="1" width="9.5" height="5" rx="1" fill="#fff"/><rect x="30.8" y="2.6" width="1" height="1.8" fill="#fff"/></svg>
  <svg class="back" width="6" height="9" viewBox="0 0 6 9"><polyline points="5,1 1.5,4.5 5,8" fill="none" stroke="#fff" stroke-width="1.2"/></svg>
  <span class="title">Settings</span>
  <span class="label" style="left:20px;top:72px">App Settings</span>
  <span class="rule" style="left:20px;top:84px;width:182px"></span>
  <span class="row" style="left:20px;top:102px">Kill Switch</span>
  <span class="toggle"><i></i></span>
  <p class="desc" style="left:20px;top:118px;width:140px">Cuts the internet connectvity when your VPN connection gets lost</p>
  <span class="row" style="left:20px;top:153px">Protocols</span>
  <svg style="left:171px;top:151px" width="10" height="11" viewBox="0 0 10 11"><path d="M5 .5L9.5 2v3.5C9.5 8 7.5 9.8 5 10.5 2.5 9.8.5 8 .5 5.5V2z" fill="#777"/><polyline points="3,5.5 4.5,7 7,4" fill="none" stroke="#fff" stroke-width=".9"/></svg>
  <span class="row" style="left:20px;top:176px">Log Out</span>
  <svg style="left:171px;top:174px" width="12" height="12" viewBox="0 0 12 12"><path d="M7 1H1v10h6M1 1l4 1.5v9L1 11" fill="none" stroke="#999" stroke-width=".8"/><path d="M8 6h4M10 4l2 2-2 2" fill="none" stroke="#999" stroke-width=".8"/></svg>
</section>

<!-- Protocols -->
<section class="screen protocols" aria-label="Protocols screen">
  <div class="header" style="height:49px"></div>
  <span class="time">9:41</span>
  <svg class="status" width="32" height="7" viewBox="0 0 32 7"><rect x="0" y="5" width="1.5" height="2" fill="#fff"/><rect x="2.3" y="3.5" width="1.5" height="3.5" fill="#fff"/><rect x="4.6" y="2" width="1.5" height="5" fill="#fff"/><rect x="6.9" y=".5" width="1.5" height="6.5" fill="#fff"/><path d="M11 3a5 5 0 0 1 7 0M12.3 4.4a3 3 0 0 1 4.4 0" stroke="#fff" stroke-width="1" fill="none"/><circle cx="14.5" cy="6" r=".9" fill="#fff"/><rect x="21" y="1" width="9.5" height="5" rx="1" fill="#fff"/><rect x="30.8" y="2.6" width="1" height="1.8" fill="#fff"/></svg>
  <svg class="back" width="6" height="9" viewBox="0 0 6 9"><polyline points="5,1 1.5,4.5 5,8" fill="none" stroke="#fff" stroke-width="1.2"/></svg>
  <span class="title">Protocols</span>
  <span class="label" style="left:21px;top:73px">Protocol Selection</span>
  <span class="rule" style="left:21px;top:86px;width:185px"></span>
  <span class="row" style="left:21px;top:103px">Automatic</span>
  <svg style="left:171px;top:103px" width="9" height="8" viewBox="0 0 9 8"><polyline points="1,4.5 3.3,6.8 8,1.2" fill="none" stroke="#f45d4c" stroke-width="1.1"/></svg>
  <p class="desc" style="left:21px;top:120px;width:110px">Let Hushnet choose the best Protocol</p>
  <span class="row" style="left:21px;top:159px">IP Sec</span>
  <p class="desc" style="left:21px;top:177px;width:150px">The Most Secure Protocol</p>
  <span class="row" style="left:21px;top:205px">IKEv2</span>
  <p class="desc" style="left:21px;top:222px;width:150px">The Most Stable Protocol</p>
</section>

</body>
</html>
```